Visitenkarten-Design für Catering/ Liefertouren
Vielen Dank für die professionelle Zusammenarbeit. Änderungen wurden schnell und treffend umgesetzt. Wir sind mit dem Ergebnis sehr zufrieden.
Zielgruppe
Catering/ Liefertouren für hochwertige selbstgemachte Quiches/ französische Tartes, Suppen, Currys
Aufgabenstellung
2 Visitenkarten im Format DIN6 (21x10,5) lang die sich auf der 1. (Bild) Seite unterscheiden aber mit identischer 2. Seite.
Karte 'Quiche' 1. Seite:
'Quiche '
Quiche Passion - depuis 2003
Quiches, Soups, Currys,
Catering, Abholung, Liefertouren
www.Kovendo.de,
info@kovendo.de
Karte 'Soups' 1. Seite:
'KovendoChicken, KovendoTofu'
2. Seite (für beide Karten identisch)
Seite soll eine Art Vorlage sein und besteht lediglich aus einer gestalterischen 'Umrahmung' und unserem Logo am unteren Seitenrand. Der Durchmesser des Logos soll max. 15% der gesamten Seitenlänge betragen.
Seite wird von uns mit Angeboten/ Aktionen bedruckt in kleiner Stückzahl nachträglich bedruckt.
1. Seiten (Quer- oder Hochformat je nach Bild möglich).
2. Seite im Hochformat.
Keine Vorgaben bzgl. Schrifttyp.

```html
<!DOCTYPE html>
<html lang="de">
<head>
<meta charset="utf-8">
<title>Kovendo Visitenkarten</title>
<link rel="stylesheet" href="https://fonts.googleapis.com/css2?family=EB+Garamond:wght@400;500&display=swap">
<style>
  :root {
    --canvas: #ebe8e8;
    --brown: #3d2320;
    --white: #ffffff;
    --slate: #3f5679;
    --slate-dark: #2c3d58;
    --paper: #ffffff;
  }
  * { margin: 0; padding: 0; box-sizing: border-box; }
  html, body { width: 1200px; height: 767px; overflow: hidden; }
  body {
    position: relative;
    background: var(--canvas);
    font-family: "EB Garamond", Georgia, serif;
    color: var(--white);
  }
  .card-front { position: absolute; left: 92px; width: 632px; }
  .card-quiche { top: 59px; }
  .card-soups { top: 402px; }

  .service-band {
    height: 27px;
    background: var(--brown);
    text-align: center;
    font-size: 13.5px;
    line-height: 27px;
    letter-spacing: 0.3px;
  }
  .card-soups .service-band { height: 29px; line-height: 29px; }

  .hero {
    position: relative;
    margin-top: 4px;
    height: 242px;
    overflow: hidden;
  }
  .card-soups .hero { margin-top: 5px; height: 240px; }

  .hero-photo { position: absolute; inset: 0; }
  .photo-quiche {
    background:
      radial-gradient(circle at 66% 45%, #8a7a4c 0 30%, #5a5a36 38%, transparent 48%),
      linear-gradient(90deg, var(--slate) 0 45%, var(--slate-dark) 100%);
  }
  .photo-soups {
    background:
      radial-gradient(circle at 57% 48%, #c8572a 0 22%, #5f5f62 27%, transparent 33%),
      radial-gradient(circle at 13% 60%, #a42a20 0 10%, transparent 20%),
      radial-gradient(circle at 88% 65%, #b88a42 0 9%, transparent 16%),
      linear-gradient(90deg, #2f3a2c 0%, #343638 50%, #2d2f30 100%);
  }
  .veil {
    position: absolute; left: 0; right: 0;
    background: rgba(255,255,255,0.14);
  }
  .veil-top { top: 0; height: 21px; }
  .veil-bottom { bottom: 0; height: 34px; }
  .card-soups .veil-top { height: 30px; }
  .card-soups .veil-bottom { height: 30px; }

  .hero-title {
    position: absolute;
    font-weight: 400;
    font-size: 72px;
    line-height: 1;
    text-shadow: 0 1px 4px rgba(0,0,0,0.3);
  }
  .card-quiche .hero-title { left: 19px; top: 50px; }
  .card-soups .hero-title { left: 30px; top: 38px; }

  .hero-tagline {
    position: absolute;
    font-size: 11.5px;
    letter-spacing: 0.2px;
  }
  .card-quiche .hero-tagline { left: 84px; top: 121px; }
  .card-soups .hero-tagline { left: 35px; top: 129px; }

  .contact-band {
    margin-top: 4px;
    height: 40px;
    background: var(--brown);
    display: flex;
    justify-content: center;
    align-items: center;
    font-size: 13.5px;
    letter-spacing: 0.3px;
  }
  .contact-band span { padding: 0 16px; }
  .contact-band .divider {
    width: 1px; height: 24px; padding: 0;
    background: rgba(255,255,255,0.8);
  }

  .card-back {
    position: absolute;
    left: 803px; top: 55px;
    width: 337px; height: 669px;
    background: var(--paper);
    box-shadow: 0 3px 6px rgba(0,0,0,0.18);
  }
  .card-back svg { position: absolute; inset: 0; }
  .brand-seal {
    position: absolute;
    left: 121px; top: 534px;
    width: 104px; height: 104px;
    border-radius: 50%;
    background: var(--brown);
    color: var(--white);
    display: flex; align-items: center; justify-content: center;
    font-size: 22px;
    font-weight: 500;
  }
</style>
</head>
<body>
  <section class="card-front card-quiche">
    <div class="service-band">Quiches | Soups | Currys | Catering | Abholung | Liefertouren</div>
    <div class="hero">
      <div class="hero-photo photo-quiche" role="img" aria-label="Spinat-Quiche mit Basilikumblättern auf einem Gitter vor dunkelblauem Hintergrund"></div>
      <div class="veil veil-top"></div>
      <div class="veil veil-bottom"></div>
      <h1 class="hero-title">Quiche</h1>
      <p class="hero-tagline">Quiche Passion - depuis 2003</p>
    </div>
    <div class="contact-band">
      <span>www.kovendo.de</span><span class="divider"></span>
      <span>+49 (0) 89-4172 0815</span><span class="divider"></span>
      <span>info@kovendo.de</span>
    </div>
  </section>

  <section class="card-front card-soups">
    <div class="service-band">Quiches | Soups | Currys | Catering | Abholung | Liefertouren</div>
    <div class="hero">
      <div class="hero-photo photo-soups" role="img" aria-label="Tomatensuppe im Gusstopf mit Paprika, Zwiebel, Kräutern und Gewürzen auf dunklem Grund"></div>
      <div class="veil veil-top"></div>
      <div class="veil veil-bottom"></div>
      <h1 class="hero-title">Soups</h1>
      <p class="hero-tagline">Quiche Passion - depuis 2003</p>
    </div>
    <div class="contact-band">
      <span>www.kovendo.de</span><span class="divider"></span>
      <span>+49 (0) 89-4172 0815</span><span class="divider"></span>
      <span>info@kovendo.de</span>
    </div>
  </section>

  <section class="card-back">
    <svg width="337" height="669" viewBox="0 0 337 669" aria-hidden="true">
      <path class="frame" d="M15 595 V27 Q15 17 25 17 H313 Q323 17 323 27 V595"
            fill="none" stroke="#3d2320" stroke-width="1.5"/>
      <path class="base-line" d="M0 595 H337" fill="none" stroke="#3d2320" stroke-width="1.5"/>
    </svg>
    <div class="brand-seal">Kovendo</div>
  </section>
</body>
</html>
```